HPS business cards

(Generators . Lighting Towers . De-watering Pumps . Compressors) put under the logo please. my details are Owen Pritchard (Director) 0461527390 harbourpinesupply@postvale.net

```html
<!DOCTYPE html>
<html lang="en">
<head>
<meta charset="utf-8">
<title>HPS business cards</title>
<link rel="stylesheet" href="https://fonts.googleapis.com/css2?family=Montserrat:wght@300;400;700&display=swap">
<style>
  :root {
    --backdrop: #2b2b2b;
    --card: #151515;
    --gold: #f0a93a;
    --ink: #f4f4f4;
  }
  * { box-sizing: border-box; margin: 0; padding: 0; }
  html, body {
    width: 1200px; height: 689px; overflow: hidden;
    background: var(--backdrop);
    font-family: "Montserrat", sans-serif;
  }
  .sheet {
    position: relative; width: 1200px; height: 689px;
  }
  .card {
    position: absolute; top: 185px;
    width: 560px; height: 320px;
    background: var(--card);
    border-radius: 18px;
  }
  .card--front { left: 27px; }
  .card--back { left: 613px; }

  .wordmark {
    display: flex; align-items: center; gap: 14px;
    color: var(--gold); font-weight: 700;
    letter-spacing: 1px; text-transform: uppercase;
  }
  .wordmark__square {
    background: var(--gold); flex: none;
  }
  .card--front .wordmark {
    position: absolute; left: 0; right: 0; top: 50%;
    transform: translateY(-50%);
    justify-content: center; font-size: 34px;
  }
  .card--front .wordmark__square { width: 34px; height: 34px; }

  .card--back .wordmark {
    position: absolute; right: 34px; top: 44px; font-size: 20px;
  }
  .card--back .wordmark__square { width: 20px; height: 20px; }

  .contact {
    position: absolute; left: 38px; top: 128px; color: var(--ink);
  }
  .contact__name {
    color: var(--gold); font-weight: 700; font-size: 22px;
  }
  .contact__role {
    font-weight: 300; font-size: 15px; margin: 2px 0 12px 40px;
  }
  .contact__icons { display: flex; gap: 8px; margin: 0 0 10px 40px; }
  .contact__icons svg { width: 20px; height: 20px; }
  .contact__line {
    font-weight: 400; font-size: 14px; line-height: 1.6;
  }
  .services {
    position: absolute; left: 38px; right: 30px; bottom: 30px;
    color: var(--ink); font-size: 14px; font-weight: 400;
    letter-spacing: 0.3px;
  }
</style>
</head>
<body>
<main class="sheet">
  <section class="card card--front" aria-label="Card front">
    <div class="wordmark">
      <span class="wordmark__square"></span>
      <span>Harbour Pine Supply</span>
    </div>
  </section>

  <section class="card card--back" aria-label="Card back">
    <div class="wordmark">
      <span class="wordmark__square"></span>
      <span>Harbour Pine Supply</span>
    </div>

    <div class="contact">
      <p class="contact__name">Owen Pritchard</p>
      <p class="contact__role">Director</p>
      <div class="contact__icons">
        <svg viewBox="0 0 20 20" aria-label="Phone">
          <circle cx="10" cy="10" r="10" fill="var(--gold)"/>
          <path d="M6 5.5c1-.8 1.6-.4 2 .4l.6 1.3c.2.5 0 .9-.4 1.2l-.5.3c.5 1.3 1.3 2.1 2.6 2.7l.4-.5c.3-.4.8-.5 1.2-.3l1.3.6c.8.4 1.1 1 .3 2-1 1.2-2.8 1-4.7-.6-1.9-1.6-3.6-4-2.8-7.1z" fill="#fff"/>
        </svg>
        <svg viewBox="0 0 20 20" aria-label="Email">
          <circle cx="10" cy="10" r="10" fill="var(--gold)"/>
          <rect x="5" y="6.5" width="10" height="7" fill="#fff"/>
          <path d="M5 6.5l5 4 5-4" fill="none" stroke="var(--gold)" stroke-width="1"/>
        </svg>
      </div>
      <p class="contact__line">0461527390</p>
      <p class="contact__line">harbourpinesupply@postvale.net</p>
    </div>

    <p class="services">Generators . Lighting Towers . De-watering Pumps . Compressors</p>
  </section>
</main>
</body>
</html>
```